Love pets? Create a veterinary business card that aligns with our new revamped website.

Greetings! We are a five-doctor veterinary hospital that seeks your expertise in designing a new business card that harmonizes with our recently revitalized website: www.lmcr.net. The card should feature our logo, the five doctors, operating hours, contact information, and communicate our purpose and personality.

Contact Information for Business Card

TBA

```html
<!DOCTYPE html>
<html lang="en">
<head>
<meta charset="utf-8">
<title>Laurel Meadow Veterinary Hospital – Business Card</title>
<link rel="stylesheet" href="https://fonts.googleapis.com/css2?family=Roboto:wght@400;500&display=swap">
<style>
  :root {
    --stage: #4a4a4a;
    --card: #1a1a1a;
    --green: #3f8f3a;
    --brown: #8a6a2c;
    --white: #ffffff;
  }
  html, body {
    margin: 0;
    padding: 0;
    width: 1200px;
    height: 801px;
    overflow: hidden;
    background: var(--stage);
    font-family: "Roboto", Arial, sans-serif;
  }
  .stage {
    position: relative;
    width: 1200px;
    height: 801px;
    display: flex;
    align-items: center;
    justify-content: center;
    gap: 50px;
  }
  .card {
    position: relative;
    width: 525px;
    height: 300px;
    background: var(--card);
    border: 2px solid var(--green);
    box-sizing: border-box;
    box-shadow: 0 14px 30px rgba(0,0,0,.45);
  }
  /* Back side */
  .card-back .brand {
    position: absolute;
    left: 34px;
    top: 128px;
    display: flex;
    align-items: center;
    gap: 10px;
  }
  .brand-dot {
    width: 18px;
    height: 18px;
    border-radius: 50%;
    background: var(--green);
    flex: none;
  }
  .brand-name {
    color: var(--green);
    font-weight: 500;
    font-size: 14px;
    line-height: 1.2;
    letter-spacing: .3px;
  }
  .divider {
    position: absolute;
    left: 262px;
    top: 32px;
    bottom: 32px;
    width: 1px;
    background: var(--green);
  }
  .contact {
    position: absolute;
    left: 286px;
    top: 36px;
    right: 20px;
    color: var(--white);
    font-size: 13px;
    line-height: 1.45;
  }
  .person-name {
    color: var(--green);
    font-size: 19px;
    font-style: italic;
    letter-spacing: 1px;
    text-transform: uppercase;
    margin: 0;
  }
  .person-title {
    margin: 0 0 12px;
    font-size: 14px;
  }
  .contact-list {
    list-style: none;
    margin: 0 0 14px;
    padding: 0;
  }
  .contact-list li {
    display: flex;
    align-items: center;
    gap: 8px;
  }
  .contact-list svg {
    width: 12px;
    height: 12px;
    fill: var(--green);
    flex: none;
  }
  .address { margin: 0; }
  /* Front side */
  .card-front .brand {
    position: absolute;
    inset: 0;
    display: flex;
    align-items: center;
    justify-content: center;
    gap: 18px;
  }
  .card-front .brand-dot { width: 54px; height: 54px; }
  .card-front .brand-name { font-size: 32px; line-height: 1.15; }
</style>
</head>
<body>
<main class="stage">
  <section class="card card-back" aria-label="Business card, contact side">
    <div class="brand">
      <span class="brand-dot"></span>
      <span class="brand-name">Laurel Meadow<br>Veterinary Hospital</span>
    </div>
    <div class="divider"></div>
    <div class="contact">
      <p class="person-name">Dale Porter</p>
      <p class="person-title">Managing Director</p>
      <ul class="contact-list">
        <li><svg viewBox="0 0 24 24"><path d="M6.6 10.8a15 15 0 0 0 6.6 6.6l2.2-2.2a1 1 0 0 1 1-.25 11 11 0 0 0 3.6.6 1 1 0 0 1 1 1V20a1 1 0 0 1-1 1A17 17 0 0 1 3 4a1 1 0 0 1 1-1h3.5a1 1 0 0 1 1 1 11 11 0 0 0 .6 3.6 1 1 0 0 1-.25 1z"/></svg>(555) 214-6082</li>
        <li><svg viewBox="0 0 24 24"><path d="M4 8h3v13H4zM9 4h9v5H9zM8 10h13v11H8zm3 2v2h2v-2zm4 0v2h2v-2zm-4 4v2h2v-2zm4 0v2h2v-2z"/></svg>(555) 214-6090</li>
        <li><svg viewBox="0 0 24 24"><path d="M2 5h20v14H2zm2 2v.5l8 5 8-5V7z"/></svg>info@lmcr.net</li>
        <li><svg viewBox="0 0 24 24"><path d="M12 2a10 10 0 1 0 0 20 10 10 0 0 0 0-20zm-1 17.9A8 8 0 0 1 4.1 11H8v2l3 3zM17.9 16.4A2 2 0 0 0 16 15h-1v-3H9v-2h2V8h2V6.1a8 8 0 0 1 4.9 10.3z"/></svg>www.lmcr.net</li>
      </ul>
      <p class="address">2048 Birchwood Lane,<br>Cedar Falls, TX 75012</p>
    </div>
  </section>

  <section class="card card-front" aria-label="Business card, brand side">
    <div class="brand">
      <span class="brand-dot"></span>
      <span class="brand-name">Laurel Meadow<br>Veterinary Hospital</span>
    </div>
  </section>
</main>
</body>
</html>
```